8x8 Social Media Ad - Summit Harbor Expo

Attention Real Estate Agents
Please join us for our
Quarterly Real Estate Training Expo
The 2nd Saturday of February, May, August and November
Our Next Training Expo is _________________________________
From 9 am to 1 pm
at
Marlowe Suites Fernfield Oak Ridge
4187 Copper Meadow Lane, Fernfield, MD 20994
Scheduled Speakers
9:00 am - Malcolm Prewitt - Orientation
9:30 am - Darnell Ockley - Multiple Income Streams / Pivot Program
10:00 am - Keira Lindqvist - Marketing though Social Media
10:45 am - Owen Trask - Generating Business through Lumo-Net
11:30 am - Ada Nwachime - Real Estate Investing
12:15 pm - Gregory Tamsin - (Main Speaker) Training Topic TBA
For more information call Malcolm Prewitt at (240) 555-0182 or email mprewitt@summitharborhomes.example

```html
<!DOCTYPE html>
<html lang="en">
<head>
<meta charset="utf-8">
<title>Summit Harbor Expo – Quarterly Real Estate Training Expo</title>
<link href="https://fonts.googleapis.com/css2?family=Oswald:wght@500;600&family=Poppins:wght@300;400;500;600;700;800&display=swap" rel="stylesheet">
<style>
  :root{
    --teal:#0e8896;
    --teal-dark:#0b7380;
    --ink:#2b2b2b;
    --charcoal:#2e2e2e;
    --white:#ffffff;
    --red:#ee0000;
    --amber:#f6b400;
    --amber-dark:#c98b00;
    --grey-bar:#6f6f6f;
    --pill:#e9e9e9;
  }
  *{margin:0;padding:0;box-sizing:border-box}
  html,body{width:1200px;height:1200px;overflow:hidden;background:var(--white)}
  body{font-family:"Poppins",sans-serif;color:var(--ink)}
  .ad{position:relative;width:1200px;height:1200px;background:var(--white);overflow:hidden}
  .abs{position:absolute}

  /* hero */
  .hero-shapes{position:absolute;left:0;top:0}
  .hero-photo{position:absolute;left:0;top:0;width:1200px;height:532px;
    background:linear-gradient(160deg,#e9dcc6 0%,#c9a782 28%,#6f5846 55%,#2d2b2e 100%);
    clip-path:polygon(762px 0,1200px 0,1200px 532px,806px 532px,717px 397px,646px 248px)}
  .attention{left:65px;top:80px;width:452px;height:95px;background:var(--red)}
  .attention span{position:absolute;left:30px;top:-6px;font-family:"Oswald",sans-serif;font-weight:600;
    font-size:86px;letter-spacing:-1px;color:var(--white);line-height:1.15;transform:scaleX(.86);transform-origin:left}
  .bang{left:419px;top:66px;width:83px;height:121px}
  .agents{left:63px;top:192px;font-weight:800;font-size:44px;color:var(--teal);letter-spacing:.3px}
  .join{left:65px;top:278px;font-weight:300;font-size:27px;color:var(--white)}
  .quarterly{left:64px;top:322px;font-weight:300;font-size:46px;color:var(--white);line-height:1}
  .expo-title{left:62px;top:362px;font-weight:800;font-size:71px;color:var(--white);line-height:1;letter-spacing:-.5px}

  /* date band */
  .date-band{left:0;top:542px;width:1200px;height:148px;background:var(--charcoal)}
  .saturday{left:65px;top:556px;font-family:"Oswald",sans-serif;font-weight:500;font-size:72px;line-height:1;
    color:var(--white);transform:scaleX(.82);transform-origin:left;letter-spacing:-1px}
  .saturday em{font-style:normal;color:var(--teal)}
  .months{left:65px;top:638px;font-size:18.5px;color:var(--white);font-weight:400}
  .months b{font-weight:700}
  .divider{left:555px;top:570px;height:96px;border-left:2px dashed #d8d8d8}
  .next{left:591px;top:566px;font-size:19px;color:var(--white);font-weight:400}
  .next-rule{left:591px;top:612px;width:252px;border-top:1px solid #8a8a8a}
  .hours{left:592px;top:626px;width:221px;height:34px;border-radius:17px;background:var(--teal);
    color:var(--white);font-size:18px;text-align:center;line-height:34px}
  .hours b{font-weight:700}
  .pin{left:880px;top:567px;width:28px;height:40px}
  .venue{left:908px;top:570px;font-size:16px;color:var(--white);line-height:19px}
  .venue p+p{margin-top:10px}

  /* speakers */
  .speakers-title{left:68px;top:716px;font-weight:700;font-size:36px;color:#1e1e1e;letter-spacing:.3px}
  .speakers-rule{left:523px;top:738px;width:406px;border-top:1px solid #9a9a9a}
  .card{top:848px;width:159px;height:142px;border-radius:10px}
  .card.teal{background:var(--teal)}
  .card.dark{background:var(--charcoal)}
  .card::after{content:"";position:absolute;inset:8px 8px 18px 8px;border:1.5px dashed rgba(255,255,255,.85);border-radius:6px}
  .portrait{top:781px;width:114px;height:114px;border-radius:50%;background:var(--white);
    border:4px solid #9bbcc1;display:flex;align-items:center;justify-content:center}
  .portrait.dark-ring{border-color:#8d8d8d}
  .portrait i{display:block;width:98px;height:98px;border-radius:50%;
    background:radial-gradient(circle at 50% 40%,#8b6a55 0%,#4a3a33 45%,#dcdcdc 46%,#e6e6e6 100%)}
  .speaker-name{top:910px;width:159px;text-align:center;font-weight:700;font-size:13.5px;color:var(--white);letter-spacing:-.2px}
  .speaker-topic{top:927px;width:159px;text-align:center;font-size:10px;line-height:11.5px;color:var(--white)}
  .time{top:957px;width:75px;height:22px;border-radius:11px;background:var(--pill);font-weight:600;
    font-size:12.5px;text-align:center;line-height:22px;color:#1e1e1e;z-index:2}

  .main-photo{left:905px;top:678px;width:252px;height:220px;
    background:linear-gradient(180deg,#ffffff 0%,#f1f1f1 30%,#6b4f40 60%,#2a2a2e 100%)}
  .main-card{left:906px;top:902px;width:251px;height:88px;background:var(--charcoal);border-radius:0 0 10px 10px}
  .main-name{left:906px;top:908px;width:251px;text-align:center;font-weight:700;font-size:19px;color:var(--white)}
  .main-role{left:906px;top:932px;width:251px;text-align:center;font-weight:600;font-size:14px;color:var(--white)}
  .main-topic{left:906px;top:950px;width:251px;text-align:center;font-size:10px;color:var(--white)}
  .main-time{left:994px;top:965px}

  /* footer */
  .brand{left:52px;top:1058px;width:250px;text-align:center;font-weight:700;font-size:24px;line-height:30px;color:var(--teal)}
  .info{left:337px;top:1053px;width:374px;text-align:right;font-weight:400;font-size:23px;color:#1e1e1e;letter-spacing:.2px}
  .contact-name{left:337px;top:1090px;width:374px;text-align:right;font-weight:700;font-size:36px;color:var(--teal);letter-spacing:.3px}
  .icon{width:26px;height:26px}
  .phone-icon{left:734px;top:1057px}
  .mail-icon{left:734px;top:1102px}
  .phone{left:768px;top:1046px;font-weight:700;font-size:33px;color:#1e1e1e}
  .email{left:768px;top:1099px;font-weight:400;font-size:19.5px;color:#1e1e1e}
  .foot-bar{left:0;top:1181px;width:1200px;height:19px;background:var(--grey-bar)}
</style>
</head>
<body>
<main class="ad">

  <!-- hero -->
  <div class="hero-photo" role="img" aria-label="Photo of a seated audience facing a speaker on stage at a conference hall"></div>
  <svg class="hero-shapes" width="1200" height="545" viewBox="0 0 1200 545" aria-hidden="true">
    <polygon points="642,0 756,0 708,91" fill="var(--teal)"/>
    <polygon points="0,270 638,270 713,400 628,532 0,532" fill="var(--teal)"/>
    <polygon points="0,270 395,270 360,318 0,318" fill="var(--charcoal)"/>
    <polygon points="646,532 720,411 795,532" fill="var(--teal)"/>
  </svg>

  <div class="abs attention"><span>ATTENTION</span></div>
  <svg class="abs bang" viewBox="0 0 83 121" aria-hidden="true">
    <polygon points="4,0 79,0 83,10 76,121 8,121 0,10" fill="var(--amber)"/>
    <polygon points="0,10 4,0 8,121" fill="var(--amber-dark)"/>
    <polygon points="83,10 79,0 76,121" fill="var(--amber-dark)"/>
    <polygon points="34,25 49,25 46,80 37,80" fill="#2a2a2a"/>
    <circle cx="41.5" cy="94" r="8" fill="#2a2a2a"/>
  </svg>
  <h2 class="abs agents">REAL ESTATE AGENTS</h2>
  <p class="abs join">Please join us for our</p>
  <p class="abs quarterly">QUARTERLY</p>
  <h1 class="abs expo-title">REAL ESTATE<br>TRAINING EXPO</h1>

  <!-- date band -->
  <section class="abs date-band"></section>
  <p class="abs saturday">THE <em>2ND SATURDAY</em></p>
  <p class="abs months">OF <b>FEBRUARY, MAY, AUGUST</b> AND <b>NOVEMBER</b></p>
  <div class="abs divider"></div>
  <p class="abs next">Our Next Training Expo is</p>
  <div class="abs next-rule"></div>
  <p class="abs hours">From <b>9 am to 1 pm</b></p>
  <svg class="abs pin" viewBox="0 0 28 40" aria-hidden="true">
    <path d="M14 0C6.3 0 0 6.1 0 13.7 0 23.5 14 40 14 40s14-16.5 14-26.3C28 6.1 21.7 0 14 0z" fill="var(--teal)"/>
    <circle cx="14" cy="13.5" r="5.5" fill="var(--charcoal)"/>
  </svg>
  <div class="abs venue">
    <p>Marlowe Suites Fernfield<br>Oak Ridge</p>
    <p>4187 Copper Meadow Lane,<br>Fernfield, MD 20994</p>
  </div>

  <!-- speakers -->
  <h3 class="abs speakers-title">SCHEDULED SPEAKERS</h3>
  <div class="abs speakers-rule"></div>

  <div class="abs card teal" style="left:64px"></div>
  <div class="abs portrait" style="left:86px" role="img" aria-label="Portrait of Malcolm Prewitt"><i></i></div>
  <p class="abs speaker-name" style="left:64px">MALCOLM PREWITT</p>
  <p class="abs speaker-topic" style="left:64px">Orientation</p>
  <p class="abs time" style="left:106px">9:00 AM</p>

  <div class="abs card dark" style="left:232px"></div>
  <div class="abs portrait dark-ring" style="left:254px" role="img" aria-label="Portrait of Darnell Ockley"><i></i></div>
  <p class="abs speaker-name" style="left:232px">DARNELL OCKLEY</p>
  <p class="abs speaker-topic" style="left:232px">Multiple Income Streams<br>Pivot Program</p>
  <p class="abs time" style="left:274px">9:00 AM</p>

  <div class="abs card teal" style="left:400px"></div>
  <div class="abs portrait" style="left:422px" role="img" aria-label="Portrait of Keira Lindqvist"><i></i></div>
  <p class="abs speaker-name" style="left:400px">KEIRA LINDQVIST</p>
  <p class="abs speaker-topic" style="left:400px">Marketing though<br>Social Media</p>
  <p class="abs time" style="left:442px">10:00 AM</p>

  <div class="abs card dark" style="left:568px"></div>
  <div class="abs portrait dark-ring" style="left:590px" role="img" aria-label="Portrait of Owen Trask"><i></i></div>
  <p class="abs speaker-name" style="left:568px">OWEN TRASK</p>
  <p class="abs speaker-topic" style="left:568px">Generating Business<br>through Lumo-Net</p>
  <p class="abs time" style="left:610px">10:45 AM</p>

  <div class="abs card teal" style="left:737px"></div>
  <div class="abs portrait" style="left:759px" role="img" aria-label="Portrait of Ada Nwachime"><i></i></div>
  <p class="abs speaker-name" style="left:737px">ADA NWACHIME</p>
  <p class="abs speaker-topic" style="left:737px">Real Estate<br>Investing</p>
  <p class="abs time" style="left:779px">11:30 AM</p>

  <div class="abs main-photo" role="img" aria-label="Portrait of main speaker Gregory Tamsin"></div>
  <div class="abs main-card"></div>
  <p class="abs main-name">GREGORY TAMSIN</p>
  <p class="abs main-role">(Main Speaker)</p>
  <p class="abs main-topic">Training Topic TBA</p>
  <p class="abs time main-time">12:15 PM</p>

  <!-- footer -->
  <p class="abs brand">SUMMIT HARBOR<br>REALTY GROUP</p>
  <p class="abs info">FOR MORE INFORMATION CALL</p>
  <p class="abs contact-name">MALCOLM PREWITT</p>
  <svg class="abs icon phone-icon" viewBox="0 0 24 24" aria-hidden="true">
    <path d="M6.6 10.8a15.1 15.1 0 0 0 6.6 6.6l2.2-2.2c.3-.3.7-.4 1-.2 1.1.4 2.3.6 3.6.6.6 0 1 .4 1 1V20c0 .6-.4 1-1 1A17 17 0 0 1 3 4c0-.6.4-1 1-1h3.5c.6 0 1 .4 1 1 0 1.3.2 2.5.6 3.6.1.3 0 .7-.2 1z" fill="none" stroke="var(--teal)" stroke-width="1.8"/>
    <path d="M15 3a6 6 0 0 1 6 6M15 6.5A2.5 2.5 0 0 1 17.5 9" fill="none" stroke="var(--teal)" stroke-width="1.6"/>
  </svg>
  <p class="abs phone">(240) 555-0182</p>
  <svg class="abs icon mail-icon" viewBox="0 0 24 24" aria-hidden="true">
    <rect x="2" y="5" width="20" height="14" fill="none" stroke="var(--teal)" stroke-width="1.8"/>
    <path d="M2 5l10 8 10-8M2 19l7.5-7M22 19l-7.5-7" fill="none" stroke="var(--teal)" stroke-width="1.6"/>
  </svg>
  <p class="abs email">mprewitt@summitharborhomes.example</p>
  <div class="abs foot-bar"></div>
</main>
</body>
</html>
```